Fresh, modern, fun business card for pediatric dental practice

Need a business card for fresh, modern, fun pediatric dental practice

Clean look that matches our website's font and colors

We prefer the look of curved corners on business cards

Target Market(s)

parents (mothers) of young children, professionals, mid-high class

Industry/Entity Type

Dental

Contact Information for Business Card

Maplewood Pediatric Dentistry
482 Corbett Lane
Suite 619
Fernbrook, ST 00000
555.555.0193
www.maplewoodtotsdental.example

Mei-Hua Tran, DMD
Colette Margrave, DMD
(we are working on our email address, but we would like that on the card as well)

Font styles to use
Sans Serif

Requirements
Must have
• All info; we would also like to make cards for individual staff members
• colors from our website and color palatte, attatched
• use same font and design as website for branding
Nice to have
• clean, simple card that has a pop of color
• we would like to see a few designs with our tag line "where smiles get brighter"
• we are not sure if we want to have it on there or not
• we would like to see a few designs incorporating the ribbon graphic on our website where the word WELCOME is

```html
<!DOCTYPE html>
<html lang="en">
<head>
<meta charset="utf-8">
<title>Maplewood Pediatric Dentistry – Business Card</title>
<link rel="stylesheet" href="https://fonts.googleapis.com/css2?family=Lato:wght@400;700&family=Raleway:wght@500&display=swap">
<style>
  :root {
    --sun: #f8bb25;
    --white: #ffffff;
    --stage: #ecebe8;
    --shadow: rgba(0, 0, 0, 0.18);
  }
  * { margin: 0; padding: 0; box-sizing: border-box; }
  html, body { width: 1200px; height: 900px; overflow: hidden; }
  body { background: var(--stage); position: relative; font-family: "Lato", sans-serif; }

  .card { position: absolute; box-shadow: 0 6px 18px var(--shadow); }

  .card-front {
    left: 178px; top: 74px; width: 588px; height: 364px;
    background: var(--sun); color: var(--white);
  }
  .card-front .dentists {
    position: absolute; right: 38px; top: 46px; text-align: right; white-space: nowrap;
    font-family: "Raleway", sans-serif; font-weight: 500; font-size: 20px; line-height: 29px;
  }
  .card-front .contacts {
    position: absolute; right: 36px; top: 166px; list-style: none; text-align: right; white-space: nowrap;
    font-size: 15px; line-height: 21.5px;
  }
  .contacts li { display: flex; justify-content: flex-end; align-items: center; gap: 4px; }
  .contacts svg { width: 13px; height: 13px; fill: var(--white); flex: none; }
  .card-front .address {
    position: absolute; right: 38px; top: 268px; text-align: right; font-style: normal; white-space: nowrap;
    font-size: 16px; line-height: 21.5px;
  }
  .address .practice { font-weight: 700; font-size: 17px; }

  .card-back {
    left: 388px; top: 505px; width: 567px; height: 352px;
    background: var(--white); color: var(--sun);
  }
  .brand {
    position: absolute; left: 0; right: 0; top: 94px; text-align: center;
    font-weight: 700; color: var(--sun);
  }
  .brand .mark { width: 46px; height: 46px; border-radius: 50%; background: var(--sun); margin: 0 auto 22px; }
  .brand .name { font-size: 46px; line-height: 46px; letter-spacing: 1px; }
  .brand .descriptor { font-size: 25px; line-height: 34px; letter-spacing: 1px; }
</style>
</head>
<body>
  <section class="card card-front" aria-label="Business card front">
    <div class="dentists">
      <p>Mei-Hua Tran, DMD</p>
      <p>Colette Margrave, DMD</p>
    </div>
    <ul class="contacts">
      <li>555.555.0193
        <svg viewBox="0 0 16 16" aria-hidden="true"><path d="M2 5c0-2 2-3 3-3l2 3-1.5 1.5c.8 1.8 2.2 3.2 4 4L11 9l3 2c0 1-1 3-3 3C6 14 2 10 2 5z"/></svg></li>
      <li>Mei-hua@maplewoodtotsdental.example
        <svg viewBox="0 0 16 16" aria-hidden="true"><path d="M1 3h14v10H1z M2 4l6 5 6-5" stroke="#f8bb25" stroke-width="1"/></svg></li>
      <li>Colette@maplewoodtotsdental.example
        <svg viewBox="0 0 16 16" aria-hidden="true"><path d="M1 3h14v10H1z M2 4l6 5 6-5" stroke="#f8bb25" stroke-width="1"/></svg></li>
      <li>www.maplewoodtotsdental.example
        <svg viewBox="0 0 16 16" aria-hidden="true"><circle cx="8" cy="8" r="7"/><path d="M1 8h14M8 1c3 3 3 11 0 14M8 1c-3 3-3 11 0 14" stroke="#f8bb25" stroke-width="1.2" fill="none"/></svg></li>
    </ul>
    <address class="address">
      <p class="practice">Maplewood Pediatric Dentistry</p>
      <p>482 Corbett Lane</p>
      <p>Suite 619 Fernbrook, ST 00000</p>
    </address>
  </section>

  <section class="card card-back" aria-label="Business card back">
    <div class="brand">
      <div class="mark" aria-hidden="true"></div>
      <p class="name">maplewood</p>
      <p class="descriptor">pediatric dentistry</p>
    </div>
  </section>
</body>
</html>
```